Paper Orchards (instructional dating book)

Title: Paper Orchards
Subtitle: Ways to charm a stranger across any crowded room
Author: R.J. Pollard
I'm seeking the title to be central with the subtitle underneath and the author slightly lower and to the left. Perhaps a border or two around the font. I thought the background could look aged (off color and old textured paper) and the background slightly punched into the texture like a typewriter has been used. I imagine it something like an old Fenwright playbook or 1940s morse code manual. Many thanks!

Target Market(s)

18 to 45 year old single people

Industry/Entity Type

Dating

Font styles to use
Serif

Requirements
Must have
• Text with border or two
Nice to have
• Traditional feel. The book is instructional.
Should not have
• Too much color or flair

```html
<!DOCTYPE html>
<html lang="en">
<head>
<meta charset="utf-8">
<title>Paper Orchards — R.J. Pollard</title>
<link rel="stylesheet" href="https://fonts.googleapis.com/css2?family=Alice&family=Cinzel:wght@500&display=swap">
<style>
  :root {
    --paper-light: #f4ebdc;
    --paper-mid: #e9dcc6;
    --paper-tan: #d9c3a2;
    --burn-edge: #7a2f0e;
    --burn-deep: #3a1306;
    --ink-rust: #8a3212;
    --ink-rust-light: #bf5e22;
    --ink-dark: #2c1f17;
    --ornament: #4a2414;
  }
  html, body {
    margin: 0;
    padding: 0;
    width: 848px;
    height: 1200px;
    overflow: hidden;
    background: var(--burn-deep);
  }
  .cover {
    position: relative;
    width: 848px;
    height: 1200px;
    overflow: hidden;
    background: var(--burn-deep);
  }
  .paper-texture {
    position: absolute;
    inset: 0;
    display: block;
  }
  .title {
    position: absolute;
    inset: 0;
    margin: 0;
    font-family: "Alice", serif;
    font-weight: 400;
  }
  .title-line {
    position: absolute;
    left: 0;
    width: 100%;
    display: block;
    text-align: center;
    line-height: 1;
    color: var(--ink-rust);
    background: linear-gradient(180deg, var(--ink-rust) 10%, var(--ink-rust-light) 55%, var(--ink-rust) 90%);
    -webkit-background-clip: text;
    background-clip: text;
    -webkit-text-fill-color: transparent;
  }
  .title-line--first { top: 55px; font-size: 245px; }
  .title-line--second { top: 445px; font-size: 190px; }
  .ornament {
    position: absolute;
    left: 372px;
    width: 104px;
    height: 30px;
    border-radius: 15px;
    background: var(--ornament);
    opacity: 0.7;
  }
  .ornament--top { top: 748px; }
  .ornament--bottom { top: 916px; }
  .subtitle {
    position: absolute;
    top: 810px;
    left: 0;
    width: 100%;
    margin: 0;
    text-align: center;
    font-family: "Cinzel", serif;
    font-weight: 500;
    font-size: 25px;
    line-height: 40px;
    letter-spacing: 0.3em;
    text-transform: uppercase;
    color: var(--ink-dark);
  }
  .author {
    position: absolute;
    top: 978px;
    left: 0;
    width: 100%;
    margin: 0;
    text-align: center;
    font-family: "Alice", serif;
    font-weight: 400;
    font-size: 108px;
    line-height: 1;
    color: var(--ink-rust);
  }
</style>
</head>
<body>
  <main class="cover">
    <svg class="paper-texture" width="848" height="1200" viewBox="0 0 848 1200" role="img" aria-label="Aged crumpled paper texture with burnt ragged edges">
      <defs>
        <radialGradient id="paperTone" cx="50%" cy="48%" r="62%">
          <stop offset="0" stop-color="#f5ecde"/>
          <stop offset="0.55" stop-color="#ebdec8"/>
          <stop offset="0.8" stop-color="#d9c1a0"/>
          <stop offset="0.93" stop-color="#b06a3a"/>
          <stop offset="1" stop-color="#7a2f0e"/>
        </radialGradient>
        <linearGradient id="edgeBurn" x1="0" y1="0" x2="0" y2="1">
          <stop offset="0" stop-color="#7a2f0e" stop-opacity="0.35"/>
          <stop offset="0.12" stop-color="#7a2f0e" stop-opacity="0"/>
          <stop offset="0.88" stop-color="#7a2f0e" stop-opacity="0"/>
          <stop offset="1" stop-color="#5a1f08" stop-opacity="0.55"/>
        </linearGradient>
        <filter id="raggedEdge" x="-5%" y="-5%" width="110%" height="110%">
          <feTurbulence type="fractalNoise" baseFrequency="0.04" numOctaves="4" seed="7" result="noise"/>
          <feDisplacementMap in="SourceGraphic" in2="noise" scale="46" xChannelSelector="R" yChannelSelector="G"/>
        </filter>
        <filter id="grain" x="0" y="0" width="100%" height="100%">
          <feTurbulence type="fractalNoise" baseFrequency="0.9" numOctaves="2" seed="3"/>
          <feColorMatrix values="0 0 0 0 0.45  0 0 0 0 0.3  0 0 0 0 0.18  0 0 0 0.22 0"/>
        </filter>
        <filter id="mottle" x="0" y="0" width="100%" height="100%">
          <feTurbulence type="fractalNoise" baseFrequency="0.012" numOctaves="3" seed="11"/>
          <feColorMatrix values="0 0 0 0 0.55  0 0 0 0 0.38  0 0 0 0 0.22  0 0 0 0.35 -0.05"/>
        </filter>
        <clipPath id="sheet">
          <rect x="26" y="18" width="796" height="1164"/>
        </clipPath>
      </defs>
      <rect class="paper-sheet" x="26" y="18" width="796" height="1164" fill="url(#paperTone)" filter="url(#raggedEdge)"/>
      <g clip-path="url(#sheet)" filter="url(#raggedEdge)">
        <rect x="26" y="18" width="796" height="1164" filter="url(#mottle)"/>
        <rect x="26" y="18" width="796" height="1164" filter="url(#grain)"/>
        <rect x="26" y="18" width="796" height="1164" fill="url(#edgeBurn)"/>
        <g class="creases" stroke="#8a6a4c" stroke-opacity="0.28" stroke-width="1.2" fill="none">
          <path d="M60 410 L220 470 L330 430 L520 520 L790 480"/>
          <path d="M120 760 L260 720 L420 790 L600 760 L800 820"/>
          <path d="M300 60 L340 260 L300 420 L360 640 L320 900 L370 1160"/>
          <path d="M600 90 L560 300 L640 560 L590 820 L650 1120"/>
          <path d="M50 1040 L240 980 L470 1060 L810 1010"/>
          <path d="M70 200 L200 150 L420 210 L780 160"/>
        </g>
      </g>
    </svg>

    <h1 class="title">
      <span class="title-line title-line--first">Paper</span>
      <span class="title-line title-line--second">Orchards</span>
    </h1>

    <div class="ornament ornament--top" role="img" aria-label="Decorative scroll flourish"></div>
    <p class="subtitle">Ways to charm a stranger<br>across any crowded room</p>
    <div class="ornament ornament--bottom" role="img" aria-label="Decorative scroll flourish"></div>

    <p class="author">R.J. Pollard</p>
  </main>
</body>
</html>
```